Van wrap - Barlev painting & Decorating

Got an orange Dornhalter vellom Long wheel base van. Looking to get signage/wrap done with the business logo on it with services we provide, 2 mobile phone numbers to go on it too. No signs or wrapping to be done on the driver, passenger and rear windows. Van is orange, so signage/wrap colours to be black/grey and white. Mix and match those colours, not all colours have to be used, for example only black and white only.

Phone numbers to be displayed are:
0412-555-018
0478-555-264

```html
<!DOCTYPE html>
<html lang="en">
<head>
<meta charset="utf-8">
<title>Barlev Painting &amp; Decorating — Van Wrap</title>
<link rel="stylesheet" href="https://fonts.googleapis.com/css2?family=Anton&family=Oswald:wght@600&family=Roboto:wght@500&display=swap">
<style>
  :root {
    --van-orange: #e8620e;
    --wrap-black: #0f0e16;
    --skirt-black: #1b1b1f;
    --glass: #3a3c42;
    --tyre: #222226;
    --hub: #c9cbd0;
    --white: #ffffff;
    --page: #ffffff;
  }
  html, body {
    margin: 0;
    width: 1200px;
    height: 1200px;
    overflow: hidden;
    background: var(--page);
  }
  .sheet { display: block; width: 1200px; height: 1200px; }
  .van-body { fill: var(--van-orange); }
  .skirt { fill: var(--skirt-black); }
  .wrap-panel { fill: var(--wrap-black); }
  .glass { fill: var(--glass); }
  .tyre { fill: var(--tyre); }
  .hub { fill: var(--hub); }
  .brush-stroke { stroke: var(--wrap-black); stroke-width: 3; stroke-linecap: round; }
  .accent-stripe { stroke: var(--white); stroke-width: 4; }
  .brand-mark { fill: var(--van-orange); }
  .brand-name {
    font-family: "Anton", sans-serif;
    fill: var(--white);
  }
  .services {
    font-family: "Oswald", sans-serif;
    font-weight: 600;
    font-size: 15px;
  }
  .services--dark { fill: var(--wrap-black); }
  .services--orange { fill: var(--van-orange); }
  .bullet { fill: var(--white); }
  .phone {
    font-family: "Roboto", sans-serif;
    font-weight: 500;
    font-size: 15px;
    fill: var(--white);
    letter-spacing: 0.5px;
  }
</style>
</head>
<body>
<svg class="sheet" viewBox="0 0 960 960" xmlns="http://www.w3.org/2000/svg" role="img" aria-label="Van wrap for Barlev Painting &amp; Decorating, two side concepts">
  <defs>
    <path id="van-shape" d="M80,135 Q80,127 95,127 L610,127 Q650,128 690,145 L770,200 Q800,225 830,272 L878,290 Q898,300 898,330 L898,380 Q898,392 885,392 L832,392 A46,46 0 0 0 740,392 L272,392 A46,46 0 0 0 180,392 L75,392 Q68,392 68,380 L70,150 Z"/>
    <clipPath id="van-clip"><use href="#van-shape"/></clipPath>
  </defs>

  <!-- Concept one: brushed black panel -->
  <g class="van van--brushed">
    <use href="#van-shape" class="van-body"/>
    <g clip-path="url(#van-clip)">
      <rect class="skirt" x="60" y="355" width="850" height="40"/>
      <path class="wrap-panel" d="M92,127 L600,127 L592,150 L604,175 L590,205 L606,235 L588,262 L598,290 L150,290 L100,284 L118,270 L90,258 L110,240 L84,220 L104,200 L88,180 L108,160 L86,142 Z"/>
      <g class="brush-stroke">
        <line x1="600" y1="140" x2="622" y2="140"/>
        <line x1="598" y1="168" x2="616" y2="168"/>
        <line x1="596" y1="198" x2="626" y2="198"/>
        <line x1="600" y1="226" x2="618" y2="226"/>
        <line x1="594" y1="254" x2="612" y2="254"/>
        <line x1="596" y1="280" x2="620" y2="280"/>
        <line x1="70" y1="165" x2="92" y2="165"/>
        <line x1="72" y1="210" x2="90" y2="210"/>
        <line x1="70" y1="250" x2="96" y2="250"/>
      </g>
    </g>
    <path class="glass" d="M622,158 L698,158 L746,215 L746,270 L622,270 Z"/>
    <circle class="tyre" cx="226" cy="395" r="38"/><circle class="hub" cx="226" cy="395" r="22"/>
    <circle class="tyre" cx="786" cy="395" r="38"/><circle class="hub" cx="786" cy="395" r="22"/>

    <circle class="brand-mark" cx="478" cy="186" r="45"/>
    <text class="brand-name" x="176" y="238" font-size="92" textLength="240" lengthAdjust="spacingAndGlyphs">BARLEV</text>
    <text class="brand-name" x="178" y="264" font-size="20" textLength="340" lengthAdjust="spacingAndGlyphs">PAINTING &amp; DECORATING</text>

    <g class="services services--dark">
      <circle class="bullet" cx="139" cy="316" r="2.5"/>
      <text x="146" y="322">INTERIOR &amp; EXTERIOR</text>
      <circle class="bullet" cx="295" cy="316" r="2.5"/>
      <text x="302" y="322">DOMESTIC</text>
      <circle class="bullet" cx="375" cy="316" r="2.5"/>
      <text x="382" y="322">INDUSTRIAL</text>
      <circle class="bullet" cx="465" cy="316" r="2.5"/>
      <text x="472" y="322">COMMERCIAL</text>
    </g>
    <text class="phone" x="618" y="322">0412-555-018</text>
    <text class="phone" x="618" y="342">0478-555-264</text>
  </g>

  <!-- Concept two: diagonal black panel -->
  <g class="van van--diagonal" transform="translate(0 410)">
    <use href="#van-shape" class="van-body"/>
    <g clip-path="url(#van-clip)">
      <rect class="skirt" x="60" y="355" width="850" height="40"/>
      <path class="wrap-panel" d="M90,127 L458,127 L628,395 L178,395 L68,238 L68,135 Z"/>
      <line class="accent-stripe" x1="474" y1="127" x2="646" y2="395"/>
      <line class="accent-stripe" x1="72" y1="262" x2="170" y2="395"/>
      <g class="brush-stroke">
        <line x1="560" y1="380" x2="660" y2="380"/>
        <line x1="580" y1="372" x2="640" y2="372"/>
        <line x1="600" y1="388" x2="690" y2="388"/>
      </g>
    </g>
    <path class="glass" d="M622,158 L698,158 L746,215 L746,270 L622,270 Z"/>
    <circle class="tyre" cx="226" cy="395" r="38"/><circle class="hub" cx="226" cy="395" r="22"/>
    <circle class="tyre" cx="786" cy="395" r="38"/><circle class="hub" cx="786" cy="395" r="22"/>

    <circle class="brand-mark" cx="432" cy="187" r="45"/>
    <text class="brand-name" x="128" y="238" font-size="92" textLength="240" lengthAdjust="spacingAndGlyphs">BARLEV</text>
    <text class="brand-name" x="130" y="264" font-size="20" textLength="340" lengthAdjust="spacingAndGlyphs">PAINTING &amp; DECORATING</text>

    <g class="services services--orange">
      <circle class="bullet" cx="193" cy="316" r="2.5"/>
      <text x="200" y="322">INTERIOR &amp; EXTERIOR</text>
      <circle class="bullet" cx="333" cy="316" r="2.5"/>
      <text x="340" y="322">DOMESTIC</text>
      <circle class="bullet" cx="409" cy="316" r="2.5"/>
      <text x="416" y="322">INDUSTRIAL</text>
      <circle class="bullet" cx="491" cy="316" r="2.5"/>
      <text x="498" y="322">COMMERCIAL</text>
    </g>
    <text class="phone" x="618" y="322">0412-555-018</text>
    <text class="phone" x="618" y="342">0478-555-264</text>
  </g>
</svg>
</body>
</html>
```